Wealth Management Business Card

We are a professional services consulting firm that specializes in high net worth individuals over $25,000,000, executives C-suite and above, closely held businesses owners, family offices and highly compensated employees.

Our focus is on risk mitigation and tax efficient strategies. Our clients take their risk on themselves and have a proven track record generating wealth. Our directive is to preserve and protect the wealth they’ve already created.

Our company Harbridge Advisory is geared around five directives of asset protection:
1) Legal Structuring
2) Leverage & Financing
3) Risk Management - Asset Protection & Insurance, Trustee Work
4) Asset Management & Investing - Under www.qelvantcapital.com
5) Tax Efficient Strategies

Our Company Mark is a Pentagon with a key in the middle. A pentagon is the most efficient defensive structure. Each point of a pentagon is equal distance front every point . Each side provides support to another and works together, which is the key to our clients success.

Our key colors are blue, black and silver.

We ‘re located in the Pacific Northwest with bi coastal and international clients. We have fewer, higher net worth clients and provide exceptional customer service. We do not do social media.

website is www.harbridgepath.com

Target Market(s)

High End Clients

Contact Information for Business Card

extra thick

Font styles to use
Serif

Requirements
Must have
• Metalic foil for lettering.
Black Background on one side
White Background on the other
Horizontal Format Only
No Rounded corners
Not Marketing sales information on the card.
Nice to have
• imprinted texture on the card
Should not have
• lots of color

```html
<!DOCTYPE html>
<html lang="en">
<head>
<meta charset="utf-8">
<title>Harbridge Advisory – Business Card</title>
<link href="https://fonts.googleapis.com/css2?family=Cinzel:wght@500;600&family=Arimo:wght@400&display=swap" rel="stylesheet">
<style>
  :root {
    --page-bg: #e4e4e6;
    --card-bg: #f7f7f8;
    --card-dark: #111214;
    --ink-blue: #1d3c8f;
    --ink-grey: #3a3a3d;
    --ink-silver: #c9ccd4;
    --tile-dark: #2a2b30;
    --tile-core: #4a6fb8;
  }
  * { box-sizing: border-box; margin: 0; padding: 0; }
  html, body { width: 1200px; height: 930px; overflow: hidden; }
  body {
    background: var(--page-bg);
    font-family: "Arimo", Arial, sans-serif;
    position: relative;
  }
  .card {
    position: absolute;
    left: 270px;
    width: 660px;
    height: 377px;
    box-shadow: 0 2px 4px rgba(0,0,0,.08), 0 14px 30px rgba(0,0,0,.10);
  }
  .card--front { top: 55px; background: var(--card-bg); }
  .card--back { top: 498px; background: var(--card-dark); }

  /* Front */
  .holder { position: absolute; left: 44px; top: 40px; }
  .holder__name {
    font-family: "Cinzel", Georgia, serif;
    font-weight: 600;
    font-size: 25px;
    letter-spacing: 1px;
    color: var(--ink-blue);
  }
  .holder__title { font-size: 17px; color: var(--ink-grey); margin-top: 2px; }

  .brand {
    position: absolute; right: 50px; top: 124px;
    display: flex; align-items: center; gap: 12px;
  }
  .brand__mark { width: 16px; height: 16px; background: var(--ink-blue); flex: none; }
  .brand__name {
    font-family: "Cinzel", Georgia, serif;
    font-weight: 600;
    font-size: 28px;
    letter-spacing: 1px;
    color: var(--ink-blue);
    white-space: nowrap;
  }

  .contact { position: absolute; left: 44px; top: 214px; list-style: none; }
  .contact__item {
    display: flex; align-items: center; gap: 8px;
    font-size: 17px; color: var(--ink-grey); line-height: 24px;
  }
  .contact__item--web { color: var(--ink-blue); }
  .contact__icon { width: 14px; height: 14px; flex: none; }

  .address {
    position: absolute; right: 50px; bottom: 36px;
    font-size: 18px; color: var(--ink-grey); line-height: 24px; text-align: left;
  }

  /* Back */
  .services { position: absolute; inset: 0; }
  .service {
    position: absolute; width: 220px;
    display: flex; flex-direction: column; align-items: center; gap: 10px;
  }
  .service__tile {
    width: 84px; height: 84px; border-radius: 50%;
    background: radial-gradient(circle, var(--tile-core) 0 30%, var(--tile-dark) 32%);
  }
  .service__label {
    font-size: 16px; color: var(--ink-silver); text-align: center; line-height: 19px;
  }
  .service--asset { left: 20px; top: 36px; }
  .service--legal { left: 220px; top: 66px; }
  .service--leverage { left: 420px; top: 96px; }
  .service--risk { left: 80px; top: 200px; }
  .service--tax { left: 300px; top: 226px; }
</style>
</head>
<body>

<section class="card card--front" aria-label="Card front">
  <div class="holder">
    <p class="holder__name">MARCUS ELLERY</p>
    <p class="holder__title">Financial Strategist and Founder</p>
  </div>

  <div class="brand">
    <span class="brand__mark"></span>
    <span class="brand__name">HARBRIDGE ADVISORY</span>
  </div>

  <ul class="contact">
    <li class="contact__item">
      <svg class="contact__icon" viewBox="0 0 16 16"><path d="M3 1h3l1.5 4-2 1.2a9 9 0 0 0 4.3 4.3L11 8.5l4 1.5v3a2 2 0 0 1-2 2A12 12 0 0 1 1 3a2 2 0 0 1 2-2z" fill="var(--ink-blue)"/></svg>
      (503) 555-0148
    </li>
    <li class="contact__item">
      <svg class="contact__icon" viewBox="0 0 16 16"><rect x="1" y="3" width="14" height="10" fill="var(--ink-blue)"/><path d="M1 3l7 6 7-6" fill="none" stroke="#fff" stroke-width="1.3"/></svg>
      info@harbridgepath.com
    </li>
    <li class="contact__item contact__item--web">
      <svg class="contact__icon" viewBox="0 0 16 16"><circle cx="8" cy="8" r="7" fill="var(--ink-blue)"/><path d="M1 8h14M8 1c-3 3.5-3 10.5 0 14M8 1c3 3.5 3 10.5 0 14" fill="none" stroke="#fff" stroke-width="1"/></svg>
      www.harbridgepath.com
    </li>
  </ul>

  <p class="address">418 Alder Crest Ave, Suite 310<br>Riverton, OR 97099</p>
</section>

<section class="card card--back" aria-label="Card back">
  <div class="services">
    <div class="service service--asset">
      <div class="service__tile" role="img" aria-label="Icon of a hand holding money"></div>
      <p class="service__label">Asset Management<br>&amp; Investing</p>
    </div>
    <div class="service service--legal">
      <div class="service__tile" role="img" aria-label="Icon of a document with a stamp"></div>
      <p class="service__label">Legal Structuring</p>
    </div>
    <div class="service service--leverage">
      <div class="service__tile" role="img" aria-label="Icon of a lever and coin"></div>
      <p class="service__label">Leverage &amp; Financing</p>
    </div>
    <div class="service service--risk">
      <div class="service__tile" role="img" aria-label="Icon of a warning sign with arrows"></div>
      <p class="service__label">Risk Management</p>
    </div>
    <div class="service service--tax">
      <div class="service__tile" role="img" aria-label="Icon of a calculator and coin"></div>
      <p class="service__label">Tax Efficient Strategies</p>
    </div>
  </div>
</section>

</body>
</html>
```